Business card design needed

I need to display a copy of one of my paintings on front,
with my contact details displayed effectively within the painting.
On the back, my Logo needs to be displayed.
Font used should be artistic, but legible.
A high quality GLOSS Paper

Target Market(s)

Business people who purchase my Art for their premises and Boardrooms but also home owners both Traditional and Modern enthusiasts.

Industry/Entity Type

Business

Contact Information for Business Card

Artist /Interior Designer- Mellie Vantorski
Specializing in Oils on Canvas
Co-ordinate Colours in Home or Office
Over 25 years experience
mobile: 0492 581064
email: rowena.k@palvix.net.au
P.O. Box 518
Marlow Reach 2947 NSW

Requirements
Must have
• Good visual of painting, well proportioned.
Your can play with the description of Artist as long as it appeals to the above clientele.
Choose a painting which allows the potential client to see the text but showcases

the canvas too.

```html
<!DOCTYPE html>
<html lang="en">
<head>
<meta charset="utf-8">
<title>Vantorski Art – Business Card</title>
<link rel="stylesheet" href="https://fonts.googleapis.com/css2?family=Great+Vibes&family=Josefin+Sans:wght@400;700&display=swap">
<style>
  :root {
    --stage: #e9e4dc;
    --card-ink: #0f0d0a;
    --card-back-top: #2a2614;
    --card-back-bottom: #0c0b07;
    --band: rgba(10, 9, 7, 0.62);
    --text-light: #f1eee6;
    --gold: #e9c21c;
    --wisteria-deep: #2b2456;
    --wisteria-mid: #5d5db8;
    --wisteria-light: #9aa3e6;
    --foliage: #4b6a22;
  }
  * { margin: 0; padding: 0; box-sizing: border-box; }
  html, body {
    width: 1200px; height: 1000px; overflow: hidden;
    background: var(--stage);
  }
  .stage {
    position: relative; width: 1200px; height: 1000px;
    display: flex; flex-direction: column; align-items: center; justify-content: center;
    gap: 44px;
  }
  .card {
    position: relative; width: 740px; height: 430px;
    overflow: hidden; border-radius: 4px;
    box-shadow: 0 10px 28px rgba(0,0,0,0.28);
  }

  /* Front */
  .card-front { background: var(--card-ink); }
  .painting {
    position: absolute; inset: 0;
    background:
      radial-gradient(ellipse 28% 42% at 30% 30%, var(--wisteria-light) 0%, var(--wisteria-mid) 40%, transparent 75%),
      radial-gradient(ellipse 20% 34% at 72% 44%, var(--wisteria-light) 0%, var(--wisteria-mid) 40%, transparent 75%),
      radial-gradient(ellipse 30% 50% at 52% 40%, #3a2a1a 0%, transparent 70%),
      radial-gradient(ellipse 60% 60% at 50% 35%, var(--foliage) 0%, transparent 70%),
      linear-gradient(180deg, var(--wisteria-deep) 0%, #17132a 55%, var(--card-ink) 100%);
    opacity: 0.92;
  }
  .info-band {
    position: absolute; left: 0; right: 0; top: 262px; height: 122px;
    background: var(--band);
  }
  .artist {
    position: absolute; left: 46px; top: 236px;
    color: var(--text-light);
  }
  .artist-name {
    font-family: "Great Vibes", cursive;
    font-size: 40px; line-height: 1; font-weight: 400;
  }
  .artist-role {
    font-family: "Josefin Sans", sans-serif; font-weight: 700;
    font-size: 15px; letter-spacing: 0.06em; margin: 2px 0 4px 2px;
  }
  .artist-notes {
    list-style: none;
    font-family: "Josefin Sans", sans-serif; font-weight: 400;
    font-size: 15px; letter-spacing: 0.05em; line-height: 1.28;
    text-transform: uppercase; margin-left: 2px;
  }
  .contact {
    position: absolute; left: 440px; top: 270px;
    list-style: none; color: var(--text-light);
    font-family: "Josefin Sans", sans-serif; font-size: 15px;
    letter-spacing: 0.06em; line-height: 1.35; text-transform: uppercase;
  }
  .contact li { display: flex; align-items: center; gap: 10px; }
  .contact .icon { width: 14px; height: 14px; flex: none; fill: var(--gold); }
  .contact .indent { padding-left: 24px; }

  /* Back */
  .card-back {
    background: radial-gradient(ellipse 70% 80% at 40% 20%, var(--card-back-top) 0%, var(--card-back-bottom) 75%);
    display: flex; align-items: center; justify-content: center;
  }
  .brand { text-align: center; color: var(--gold); font-family: "Josefin Sans", sans-serif; }
  .brand-line { display: flex; align-items: center; gap: 14px; justify-content: center; }
  .brand-name { font-size: 46px; font-weight: 400; letter-spacing: 0.08em; text-transform: uppercase; }
  .brand-dot { width: 14px; height: 14px; border-radius: 50%; background: var(--gold); }
  .brand-tagline {
    margin-top: 8px; font-size: 17px; letter-spacing: 0.22em; text-transform: uppercase;
    color: var(--text-light);
  }
</style>
</head>
<body>
<main class="stage">
  <section class="card card-front" aria-label="Business card front">
    <div class="painting" role="img" aria-label="Oil painting of hanging purple wisteria blossoms with green and amber stems on a dark ground"></div>
    <div class="info-band"></div>
    <div class="artist">
      <h1 class="artist-name">Mellie Vantorski</h1>
      <p class="artist-role">ARTIST / INTERIOR DESIGNER</p>
      <ul class="artist-notes">
        <li>Specializing in oils on canvas</li>
        <li>Co-ordinate colours in home or office</li>
        <li>Over 25 years experience</li>
      </ul>
    </div>
    <ul class="contact">
      <li><svg class="icon" viewBox="0 0 16 16" aria-hidden="true"><path d="M3.5 1.5l2.5 0 1 3.5-1.8 1.2a8 8 0 0 0 4.6 4.6L11 9l3.5 1v2.5c0 1-1 2-2 2C6.5 14.5 1.5 9.5 1.5 3.5c0-1 1-2 2-2z"/></svg>0492 581064</li>
      <li><svg class="icon" viewBox="0 0 16 16" aria-hidden="true"><path d="M1 3h14v10H1z M1.5 3.5L8 9l6.5-5.5" stroke="#0f0d0a" stroke-width="1.2"/></svg>rowena.k@palvix.net.au</li>
      <li><svg class="icon" viewBox="0 0 16 16" aria-hidden="true"><path d="M8 0.5a5 5 0 0 1 5 5c0 4-5 10-5 10s-5-6-5-10a5 5 0 0 1 5-5zm0 3a2 2 0 1 0 0 4 2 2 0 0 0 0-4z"/></svg>P.O. Box 518</li>
      <li class="indent">Marlow Reach, 2947 NSW</li>
    </ul>
  </section>

  <section class="card card-back" aria-label="Business card back">
    <div class="brand">
      <div class="brand-line">
        <span class="brand-name">Vantorski Art</span>
        <span class="brand-dot" aria-hidden="true"></span>
      </div>
      <p class="brand-tagline">For Home &amp; Office</p>
    </div>
  </section>
</main>
</body>
</html>
```